Business card design for Tarvello Studios, and Event & Entertainment business

The business card design is for a new business venture, Tarvello Studios. This company offers Event management, entertainment management and also Latin dance tuition. We currently run Latin dance festivals in Australia & also teach street Latin. This business card is for the director, Wren Hollis. The Logo has already been designed. So, I need the new design to incorporate and go with the existing Logo.

The look I like is clean, simple & elegant but I also want it to be sexy. Elegant, but not corporate. Clean & simple but not boring :-)

If you want to add another design element as well as using the Logo, please use something with movement. I like ripples or swirls for example.

I would also like to have part of the card embossed or Spot UV pressed so I would like some part of the design to have texture.

Text for the Cards is as follows;

Tarvello Studios ( Logo attached )

Wren Hollis

EVENTS & ENTERTAINMENT MANAGEMENT

m: 0487 552 031
e: wren@tarvellostudios.com.au
f Tarvello Studios

www.tarvellostudios.com.au

Please try portrait layout.

Thanks, Wren
Updates

Hello Designers, Thank you to all of you who have submitted designs for Tarvello Studios. I will make up my mind now from what I have already been sent. Very close to making a decision :-) Thank you, Wren

Target Market(s)

Adults, 18 - 60 age group. People who are active. People interested in different cultures. People who like to travel. Please who like to have fun. People who are passionate about Latin dance.

Industry/Entity Type

Entertainment

Font styles to use
Sans Serif
Script

Colors
9bcb3c
ec1f27
ffffff

Requirements
Must have
• Logo + All text listed in brief
Nice to have
• An extra design feature or background image that could be embossed or spot uv pressed to add texture & flare.

```html
<!DOCTYPE html>
<html lang="en">
<head>
<meta charset="utf-8">
<title>Tarvello Studios – Business Card</title>
<link rel="stylesheet" href="https://fonts.googleapis.com/css2?family=Arimo:wght@400;700&family=Great+Vibes&display=swap">
<style>
  :root {
    --stage: #eef0ea;
    --card-bg: #ffffff;
    --ink: #1a1a1a;
    --green: #9bcb3c;
    --red: #ec1f27;
    --white: #ffffff;
  }
  html, body {
    margin: 0;
    padding: 0;
    overflow: hidden;
  }
  .stage {
    position: relative;
    width: 1200px;
    height: 654px;
    background: var(--stage);
    overflow: hidden;
  }
  .card {
    position: absolute;
    left: 400px;
    top: 0;
    width: 400px;
    height: 654px;
    box-sizing: border-box;
    background: var(--card-bg);
    overflow: hidden;
    font-family: "Arimo", Arial, sans-serif;
    color: var(--ink);
    text-align: center;
  }
  .brand {
    position: absolute;
    left: 0;
    right: 0;
    top: 58px;
  }
  .brand-mark {
    display: block;
    width: 56px;
    height: 56px;
    margin: 0 auto 22px;
    border-radius: 50%;
    background: var(--red);
  }
  .brand-name {
    margin: 0;
    font-size: 34px;
    font-weight: 400;
    line-height: 1;
    color: var(--ink);
  }
  .tagline {
    margin: 22px 0 0;
    font-size: 17px;
    font-weight: 700;
    line-height: 25px;
    letter-spacing: 0.4px;
    color: var(--green);
  }
  .divider {
    position: absolute;
    left: 60px;
    right: 60px;
    top: 302px;
    height: 2px;
    background: var(--green);
  }
  .person-name {
    position: absolute;
    left: 0;
    right: 0;
    top: 322px;
    margin: 0;
    font-family: "Great Vibes", cursive;
    font-size: 48px;
    font-weight: 400;
    line-height: 1.1;
    color: var(--red);
  }
  .contact {
    position: absolute;
    left: 50px;
    top: 410px;
    margin: 0;
    padding: 0;
    list-style: none;
    text-align: left;
  }
  .contact-item {
    display: flex;
    align-items: center;
    height: 38px;
    font-size: 19px;
  }
  .contact-icon {
    width: 24px;
    height: 26px;
    margin-right: 12px;
    flex: none;
    display: flex;
    align-items: center;
    justify-content: center;
  }
  .social-square {
    width: 13px;
    height: 19px;
    background: var(--green);
  }
  .website {
    position: absolute;
    left: 0;
    right: 0;
    top: 560px;
    margin: 0;
    font-size: 19px;
    font-weight: 700;
    color: var(--ink);
  }
  .base-band {
    position: absolute;
    left: 0;
    right: 0;
    bottom: 0;
    height: 30px;
    background: var(--green);
  }
</style>
</head>
<body>
  <div class="stage">
    <div class="card">
      <div class="brand">
        <span class="brand-mark"></span>
        <p class="brand-name">Tarvello Studios</p>
        <p class="tagline">EVENTS &amp; ENTERTAINMENT<br>MANAGEMENT</p>
      </div>

      <div class="divider"></div>

      <p class="person-name">Wren Hollis</p>

      <ul class="contact">
        <li class="contact-item">
          <span class="contact-icon">
            <svg width="22" height="26" viewBox="0 0 24 28" aria-hidden="true">
              <path d="M6 2 C4 2 2 4 2 7 C2 16 9 25 18 26 C20 26 22 24 22 22 L22 20 L16 17 L13 20 C10 18 8 14 7 11 L10 8 L8 2 Z" fill="#9bcb3c"/>
            </svg>
          </span>
          <span class="contact-text">0487 552 031</span>
        </li>
        <li class="contact-item">
          <span class="contact-icon">
            <svg width="24" height="17" viewBox="0 0 26 18" aria-hidden="true">
              <rect x="1" y="1" width="24" height="16" fill="none" stroke="#9bcb3c" stroke-width="2"/>
              <path d="M1 1 L13 10 L25 1" fill="none" stroke="#9bcb3c" stroke-width="2"/>
            </svg>
          </span>
          <span class="contact-text">wren@tarvellostudios.com.au</span>
        </li>
        <li class="contact-item">
          <span class="contact-icon"><span class="social-square"></span></span>
          <span class="contact-text">Tarvello Studios</span>
        </li>
      </ul>

      <p class="website">www.tarvellostudios.com.au</p>

      <div class="base-band"></div>
    </div>
  </div>
</body>
</html>
```